Business Card Design for Brightkeel

The company provides engineering tender consulting services and personnel resources. The target market is large engineering construction and services companies. The business is based in Australia.

```html
<!DOCTYPE html>
<html lang="en">
<head>
<meta charset="utf-8">
<title>Brightkeel — Business Card</title>
<link href="https://fonts.googleapis.com/css2?family=Open+Sans:wght@400;600;700&display=swap" rel="stylesheet">
<style>
  :root {
    --stage: #e4e4e2;
    --green-light: #b8da24;
    --green-mid: #a2c816;
    --green-dark: #84a80c;
    --lime: #b4d62a;
    --white: #ffffff;
    --back-top: #ffffff;
    --back-bottom: #e7e7e7;
    --ink: #1b1b1b;
    --blue: #2a5f9e;
    --square: #2d6fae;
  }
  * { margin: 0; padding: 0; box-sizing: border-box; }
  html, body { width: 1200px; height: 1049px; overflow: hidden; }
  body {
    position: relative;
    background: var(--stage);
    font-family: "Open Sans", Arial, sans-serif;
    color: var(--ink);
  }
  .card {
    position: absolute;
    left: 207px;
    width: 796px;
    height: 474px;
    border-radius: 12px;
    overflow: hidden;
  }
  .card--front {
    top: 43px;
    background: radial-gradient(ellipse at 50% 40%, var(--green-light) 0%, var(--green-mid) 55%, var(--green-dark) 100%);
  }
  .card--back {
    top: 528px;
    background: linear-gradient(180deg, var(--back-top) 0%, var(--back-bottom) 100%);
  }
  .trim { position: absolute; left: 0; top: 0; }

  /* front */
  .brand-mark {
    position: absolute;
    left: 146px; top: 160px;
    width: 107px; height: 107px;
    background: var(--white);
    opacity: .9;
  }
  .brand-name {
    position: absolute;
    font-weight: 600;
    white-space: nowrap;
  }
  .card--front .brand-name {
    left: 344px; top: 140px;
    font-size: 46px;
    color: var(--white);
  }
  .contact {
    position: absolute;
    font-size: 16px;
    color: var(--ink);
    white-space: nowrap;
    display: flex;
    align-items: center;
    gap: 12px;
  }
  .contact svg { width: 20px; height: 20px; fill: var(--ink); }
  .contact--phone1 { left: 321px; top: 212px; }
  .contact--phone2 { left: 321px; top: 246px; }
  .contact--email { left: 489px; top: 212px; }
  .contact--address { left: 489px; top: 246px; }
  .contact .value { letter-spacing: .5px; }
  .divider {
    position: absolute;
    left: 473px; top: 205px;
    width: 1px; height: 72px;
    background: var(--ink);
    opacity: .6;
  }
  .reg {
    position: absolute;
    left: 370px; top: 290px;
    font-size: 16px;
    letter-spacing: .6px;
    white-space: nowrap;
  }
  .reg .label { color: var(--white); font-size: 14px; margin-right: 12px; }

  /* back */
  .card--back .brand-name {
    left: 488px; top: 40px;
    font-size: 27px;
    color: var(--blue);
  }
  .card--back .brand-mark {
    left: 713px; top: 32px;
    width: 42px; height: 42px;
    background: var(--square);
    opacity: 1;
  }
  .points {
    position: absolute;
    left: 30px; top: 79px;
    list-style: none;
    font-size: 17px;
    line-height: 27.2px;
  }
  .points li { display: flex; align-items: center; white-space: nowrap; }
  .points li::before {
    content: "";
    width: 0; height: 0;
    border-left: 16px solid var(--blue);
    border-top: 6px solid transparent;
    border-bottom: 6px solid transparent;
    margin-right: 9px;
  }
  .points .lead { width: 158px; }
  .person {
    position: absolute;
    right: 26px; top: 356px;
    text-align: right;
  }
  .person .name { font-size: 30px; letter-spacing: 1.5px; line-height: 36px; color: var(--ink); }
  .person .first { color: var(--blue); }
  .person .role { font-size: 16px; font-weight: 700; letter-spacing: 1.4px; margin-right: 14px; }
  .web {
    position: absolute;
    left: 21px; top: 413px;
    font-size: 17px;
    font-weight: 700;
  }
</style>
</head>
<body>

<section class="card card--front" aria-label="Card front">
  <svg class="trim" width="796" height="474" viewBox="0 0 796 474" aria-hidden="true">
    <g fill="#ffffff">
      <rect x="13" y="4" width="40" height="10"/><rect x="76" y="4" width="40" height="10"/>
      <rect x="139" y="4" width="40" height="10"/><rect x="202" y="4" width="40" height="10"/>
      <rect x="265" y="4" width="40" height="10"/><rect x="328" y="4" width="40" height="10"/>
      <rect x="391" y="4" width="40" height="10"/><rect x="454" y="4" width="40" height="10"/>
      <rect x="517" y="4" width="40" height="10"/><rect x="580" y="4" width="40" height="10"/>
      <rect x="643" y="4" width="40" height="10"/>
      <polygon points="700,4 750,4 737,-10 790,17 737,32 748,14 700,14"/>
    </g>
    <g fill="#c5e34a">
      <rect x="120" y="446" width="40" height="28"/><rect x="183" y="446" width="40" height="28"/>
      <rect x="246" y="446" width="40" height="28"/><rect x="309" y="446" width="40" height="28"/>
      <rect x="372" y="446" width="40" height="28"/><rect x="435" y="446" width="40" height="28"/>
      <rect x="498" y="446" width="40" height="28"/><rect x="561" y="446" width="40" height="28"/>
      <rect x="624" y="446" width="40" height="28"/><rect x="687" y="446" width="40" height="28"/>
      <rect x="750" y="446" width="40" height="28"/>
      <polygon points="110,446 50,446 62,432 10,460 62,474 110,474"/>
    </g>
  </svg>

  <div class="brand-mark" aria-hidden="true"></div>
  <div class="brand-name">Brightkeel</div>

  <div class="contact contact--phone1">
    <span class="value">999 999 999</span>
    <svg viewBox="0 0 20 20"><rect x="6" y="1" width="9" height="18" rx="2"/><rect x="8" y="3.5" width="5" height="7" fill="#b0d41e"/></svg>
  </div>
  <div class="contact contact--phone2">
    <span class="value">999 999 999</span>
    <svg viewBox="0 0 20 20"><path d="M1 8c0-3 4-5 9-5s9 2 9 5v2h-4V8H5v2H1z"/><path d="M4 11h12l2 7H2z"/></svg>
  </div>
  <div class="divider"></div>
  <div class="contact contact--email">
    <svg viewBox="0 0 20 20"><rect x="2" y="5" width="16" height="11"/><path d="M2 5l8 6 8-6" fill="none" stroke="#b0d41e" stroke-width="1.5"/></svg>
    <span class="value">nnnn@nnn.com.au</span>
  </div>
  <div class="contact contact--address">
    <svg viewBox="0 0 20 20"><path d="M10 2L1 10h3v8h4v-5h4v5h4v-8h3z"/></svg>
    <span class="value">99,Nnnnnnnnn,Nnn,9999</span>
  </div>
  <div class="reg"><span class="label">RegNo</span>ABN99999999999</div>
</section>

<section class="card card--back" aria-label="Card back">
  <svg class="trim" width="796" height="474" viewBox="0 0 796 474" aria-hidden="true">
    <g fill="#ffffff">
      <rect x="13" y="459" width="40" height="10"/><rect x="76" y="459" width="40" height="10"/>
      <rect x="139" y="459" width="40" height="10"/><rect x="202" y="459" width="40" height="10"/>
      <rect x="265" y="459" width="40" height="10"/><rect x="328" y="459" width="40" height="10"/>
      <rect x="391" y="459" width="40" height="10"/><rect x="454" y="459" width="40" height="10"/>
      <rect x="517" y="459" width="40" height="10"/><rect x="580" y="459" width="40" height="10"/>
      <rect x="643" y="459" width="40" height="10"/>
      <polygon points="700,459 750,459 737,445 790,469 737,490 748,469 700,469"/>
    </g>
    <rect x="0" y="0" width="796" height="3" fill="#b4d62a"/>
  </svg>

  <div class="brand-name">Brightkeel</div>
  <div class="brand-mark" aria-hidden="true"></div>

  <ul class="points">
    <li><span class="lead">Your Text is here</span>Your Text is here Your Text is here...</li>
    <li><span class="lead">Your Text is here</span>Your Text is here Your Text is here...</li>
    <li><span class="lead">Your Text is here</span>Your Text is here Your Text is here...</li>
    <li><span class="lead">Your Text is here</span>Your Text is here Your Text is here...</li>
    <li><span class="lead">Your Text is here</span>Your Text is here Your Text is here...</li>
    <li><span class="lead">Your Text is here</span>Your Text is here Your Text is here...</li>
    <li><span class="lead">Your Text is here</span>Your Text is here Your Text is here...</li>
    <li><span class="lead">Your Text is here</span>Your Text is here Your Text is here...</li>
    <li><span class="lead">Your Text is here</span>Your Text is here Your Text is here...</li>
    <li><span class="lead">Your Text is here</span>Your Text is here Your Text is here...</li>
  </ul>

  <div class="person">
    <div class="name"><span class="first">Dana</span> Whitlow</div>
    <div class="role">General Manager</div>
  </div>
  <div class="web">www.brightkeel.com</div>
</section>

</body>
</html>
```